Now Hiring Drivers or Help Wanted Ad

I am looking for an ad to be used for digital marketing for employment. Below is some or all of the information to work into the ad.

CRANE Holdings, LLC is a stable and premier hauler operating in the Northeast Wisconsin region since 1994. We have a variety of equipment from Dump Trucks, Roll Off Trucks to Semis with Belt Trailers, Walking Floors, Gondolas, Tankers, Vans and Compacting Trailers offering a variety of positions with different routes to mix up your day or settle into something you enjoy. We also offer low boy services and some flat bed work. We haul various materials from general aggregate freight to various types of non-hazardous wastes such as garbage, recyclables, paper mill sludge, metal, shredder fluff to various landfills or recycling centers.

Rate of pay is based on experience and the variety of equipment you are able to operate or your willingness to learn.

All work is local and you are home every night.

Great Pay
Sign on Bonus
Holiday & Vacation Pay
Health Insurance, Vision & Dental Offered
Employer Paid Life Insurance
Uniforms
Phone Reimbursement
VORIX

Industry/Entity Type

Trucking and Excavation

Colors
EB3D1F
EC4F4E
F09395
F8D3D4
FCEDEE

Requirements
Must have
• Should have some of the same look/feel of the ad attached.

```html
<!DOCTYPE html>
<html lang="en">
<head>
<meta charset="utf-8">
<title>Now Hiring Drivers – CRANE Holdings, LLC</title>
<link rel="stylesheet" href="https://fonts.googleapis.com/css2?family=Alfa+Slab+One&family=Montserrat:wght@700&family=Roboto+Slab:wght@400;700&family=Roboto:wght@700&display=swap">
<style>
  :root {
    --red: #e31e24;
    --red-deep: #c9232a;
    --yellow: #f5c60d;
    --ink: #1b1b1b;
    --white: #ffffff;
    --green: #4caf50;
    --sky-top: #3f8fd6;
    --sky-bottom: #ffffff;
    --photo-light: #d9dde2;
    --photo-mid: #e0585d;
    --photo-dark: #b51d23;
  }
  * { margin: 0; padding: 0; box-sizing: border-box; }
  html, body { width: 990px; height: 1200px; overflow: hidden; background: var(--white); }
  .flyer {
    position: relative; width: 990px; height: 1200px; overflow: hidden;
    background: linear-gradient(180deg, var(--sky-top) 0%, #a9d0ef 22%, var(--sky-bottom) 45%);
  }
  .photo {
    position: absolute; left: 0; top: 250px; width: 990px; height: 560px;
    background:
      radial-gradient(ellipse 420px 300px at 430px 330px, var(--photo-mid) 0%, rgba(224,88,93,0) 100%),
      linear-gradient(115deg, var(--photo-light) 0%, #c3c7cc 22%, var(--photo-dark) 48%, var(--photo-mid) 70%, #d4d7db 100%);
    -webkit-mask-image: linear-gradient(180deg, transparent 0%, #000 22%);
    mask-image: linear-gradient(180deg, transparent 0%, #000 22%);
  }
  .waves { position: absolute; left: 0; top: 0; }
  .headline {
    position: absolute; left: 0; width: 990px; text-align: center;
    font-family: "Alfa Slab One", "Roboto Slab", serif; font-weight: 400; color: var(--red);
    -webkit-text-stroke: 3px var(--white); paint-order: stroke fill;
    text-shadow: 5px 5px 0 var(--ink);
    line-height: 1;
  }
  .headline--top { top: 82px; font-size: 104px; letter-spacing: 1px; }
  .headline--bottom { top: 202px; font-size: 104px; }
  .promise {
    position: absolute; left: 640px; top: 362px; width: 270px; height: 270px;
    border-radius: 50%; background: var(--yellow);
    display: flex; align-items: center; justify-content: center; text-align: center;
    font-family: "Roboto Slab", serif; font-weight: 700; font-size: 29px; line-height: 1.2;
    color: var(--ink);
  }
  .promise-ring { position: absolute; left: 612px; top: 332px; }
  .benefits {
    position: absolute; left: 88px; top: 800px; list-style: none;
    font-family: "Roboto Slab", serif; font-weight: 700; font-size: 25px; color: var(--white);
  }
  .benefits li { display: flex; align-items: center; height: 45.5px; white-space: nowrap; }
  .benefits svg { width: 22px; height: 22px; margin-right: 14px; flex: none; }
  .brand {
    position: absolute; left: 520px; top: 788px; width: 420px; text-align: center;
  }
  .brand-name {
    display: inline-flex; align-items: center; gap: 12px; white-space: nowrap;
    font-family: "Roboto Slab", serif; font-weight: 700; font-size: 34px; line-height: 1; color: var(--green);
  }
  .brand-dot { width: 22px; height: 22px; border-radius: 50%; background: var(--white); flex: none; }
  .brand-services {
    margin-top: 12px; font-family: "Montserrat", sans-serif; font-weight: 700; font-size: 10px; color: var(--yellow);
  }
  .brand-town {
    margin-top: 8px; font-family: "Montserrat", sans-serif; font-weight: 700; font-size: 13px; color: var(--green);
  }
  .phone {
    position: absolute; left: 468px; top: 1051px; width: 454px; height: 62px;
    border-radius: 31px; background: var(--ink);
    display: flex; align-items: center; padding-left: 14px;
  }
  .phone-icon { width: 44px; height: 44px; flex: none; }
  .phone-number {
    margin-left: 22px; font-family: "Roboto", sans-serif; font-weight: 700;
    font-size: 48px; color: var(--yellow); line-height: 1;
  }
  .website {
    position: absolute; left: 468px; top: 1124px; width: 454px; text-align: center;
    font-family: "Roboto Slab", serif; font-weight: 400; font-size: 20px; color: var(--ink);
    letter-spacing: 2.2px; white-space: nowrap;
  }
  .website strong { font-weight: 700; }
</style>
</head>
<body>
<main class="flyer">
  <div class="photo" role="img" aria-label="Photo of a driver in a hi-vis shirt standing beside a red dump truck parked on a road"></div>

  <svg class="waves" width="990" height="1200" viewBox="0 0 990 1200" aria-hidden="true">
    <path d="M0,730 Q260,840 560,740 Q780,660 990,575 L990,1200 L0,1200 Z" fill="var(--red)"/>
    <path d="M560,1200 Q700,1000 990,890 L990,1200 Z" fill="var(--red-deep)" opacity="0.7"/>
    <path d="M0,1160 Q360,1215 660,1070 Q830,990 990,1000 L990,1200 L0,1200 Z" fill="var(--yellow)"/>
  </svg>

  <h1 class="headline headline--top">NOW HIRING</h1>
  <h1 class="headline headline--bottom">DRIVERS</h1>

  <svg class="promise-ring" width="330" height="330" viewBox="0 0 330 330" aria-hidden="true">
    <circle cx="163" cy="160" r="150" fill="none" stroke="var(--yellow)" stroke-width="4" stroke-dasharray="700 120"/>
  </svg>
  <p class="promise">All work is<br>local and<br>you are home<br>every night.</p>

  <ul class="benefits">
    <li><svg viewBox="0 0 22 22"><circle cx="11" cy="11" r="9.5" fill="none" stroke="var(--yellow)" stroke-width="2"/><path d="M6.5 11.2l3 3 6-6" fill="none" stroke="var(--yellow)" stroke-width="2"/></svg>Great Pay</li>
    <li><svg viewBox="0 0 22 22"><circle cx="11" cy="11" r="9.5" fill="none" stroke="var(--yellow)" stroke-width="2"/><path d="M6.5 11.2l3 3 6-6" fill="none" stroke="var(--yellow)" stroke-width="2"/></svg>Sign on Bonus</li>
    <li><svg viewBox="0 0 22 22"><circle cx="11" cy="11" r="9.5" fill="none" stroke="var(--yellow)" stroke-width="2"/><path d="M6.5 11.2l3 3 6-6" fill="none" stroke="var(--yellow)" stroke-width="2"/></svg>Holiday &amp; Vacation Pay</li>
    <li><svg viewBox="0 0 22 22"><circle cx="11" cy="11" r="9.5" fill="none" stroke="var(--yellow)" stroke-width="2"/><path d="M6.5 11.2l3 3 6-6" fill="none" stroke="var(--yellow)" stroke-width="2"/></svg>Health Insurance, Vision &amp; Dental Offered</li>
    <li><svg viewBox="0 0 22 22"><circle cx="11" cy="11" r="9.5" fill="none" stroke="var(--yellow)" stroke-width="2"/><path d="M6.5 11.2l3 3 6-6" fill="none" stroke="var(--yellow)" stroke-width="2"/></svg>Employer Paid Life Insurance</li>
    <li><svg viewBox="0 0 22 22"><circle cx="11" cy="11" r="9.5" fill="none" stroke="var(--yellow)" stroke-width="2"/><path d="M6.5 11.2l3 3 6-6" fill="none" stroke="var(--yellow)" stroke-width="2"/></svg>Uniforms</li>
    <li><svg viewBox="0 0 22 22"><circle cx="11" cy="11" r="9.5" fill="none" stroke="var(--yellow)" stroke-width="2"/><path d="M6.5 11.2l3 3 6-6" fill="none" stroke="var(--yellow)" stroke-width="2"/></svg>Phone Reimbursement</li>
    <li><svg viewBox="0 0 22 22"><circle cx="11" cy="11" r="9.5" fill="none" stroke="var(--yellow)" stroke-width="2"/><path d="M6.5 11.2l3 3 6-6" fill="none" stroke="var(--yellow)" stroke-width="2"/></svg>VORIX</li>
  </ul>

  <div class="brand">
    <div class="brand-name"><span class="brand-dot"></span>CRANE Holdings, LLC</div>
    <p class="brand-services">BRUSH CUTTING . EXCAVATING . SNOW REMOVAL . TRUCKING</p>
    <p class="brand-town">FOX BEND, WI</p>
  </div>

  <div class="phone">
    <svg class="phone-icon" viewBox="0 0 44 44" aria-hidden="true">
      <circle cx="22" cy="22" r="21" fill="var(--yellow)"/>
      <path d="M15 11c1-1 2.5-1 3.2.2l2.3 3.8c.6 1 .3 2.2-.6 2.9l-1.6 1.2c1.2 2.8 3.3 5 6 6.2l1.3-1.6c.7-.9 2-1.1 2.9-.5l3.8 2.4c1.1.7 1.2 2.2.2 3.2l-1.8 1.8c-1.3 1.3-3.3 1.6-5 .9-6.2-2.6-11-7.5-13.5-13.7-.7-1.7-.3-3.7 1-5z" fill="var(--ink)"/>
    </svg>
    <span class="phone-number">920-555-0143</span>
  </div>
  <p class="website">www.<strong>CraneHoldingsLLC</strong>.com</p>
</main>
</body>
</html>
```